Funeral Services Web Site

We need a website for a Funeral Services company. The choice of colors is free of charge. One Page Website with 8 sections. Menu: - Home - Our Services - Obituaries -> link to another page. - Our Shop - Funeral Monument - Funeral Contract - Contact Us

Target Market(s)

Every one need Funeral Services

Coding

Coded - Design and coding required

Number of Pages Required

2 page

Font styles to use
Sans Serif
Script

Colors

Designer to choose colors to be used in the design.

```html
<!DOCTYPE html>
<html lang="en">
<head>
<meta charset="utf-8">
<title>Site Footer – Maison Verlaine</title>
<link rel="stylesheet" href="https://fonts.googleapis.com/css2?family=Cinzel:wght@400&family=Quattrocento+Sans:ital@0;1&display=swap">
<style>
  :root {
    --bg: #faf9f7;
    --text: #a29d98;
    --text-strong: #7d7772;
    --heading: #6e5d4d;
    --brand: #6e5d4d;
    --tile-border: #e8e4df;
    --icon: #a8a39e;
    --quote: #e4e0da;
  }
  * { box-sizing: border-box; margin: 0; padding: 0; }
  html, body { width: 1200px; height: 475px; overflow: hidden; }
  body {
    background: var(--bg);
    font-family: "Quattrocento Sans", Arial, sans-serif;
    color: var(--text);
    font-size: 13px;
    line-height: 21.6px;
  }
  .site-footer { position: relative; width: 1200px; height: 475px; border-top: 2px solid #efedea; }
  .footer-col { position: absolute; top: 64px; width: 236px; }
  .col-about { left: 88px; top: 70px; }
  .col-testimonials { left: 352px; }
  .col-contact { left: 615px; }
  .col-gallery { left: 878px; }

  .col-heading {
    font-family: "Cinzel", Georgia, serif;
    font-weight: 400;
    font-size: 18px;
    letter-spacing: 0.3px;
    color: var(--heading);
    margin-bottom: 20px;
  }

  .brand {
    display: flex; align-items: center; gap: 12px;
    height: 146px;
    font-family: "Quattrocento Sans", Arial, sans-serif;
    font-size: 22px;
    color: var(--brand);
  }
  .brand-mark { width: 14px; height: 14px; background: var(--brand); border-radius: 50%; }
  .about-text { margin-top: 52px; width: 232px; }

  .social-list { display: flex; gap: 12px; margin-top: 32px; list-style: none; }
  .social-tile {
    width: 38px; height: 38px;
    border: 3px solid var(--tile-border);
    background: var(--bg);
  }

  .testimonial { position: relative; width: 236px; }
  .testimonial-quote-mark {
    position: absolute; left: -2px; top: -14px;
    font-family: Georgia, serif; font-size: 44px; color: var(--quote); line-height: 1;
  }
  .testimonial-body { position: relative; }
  .testimonial-author { margin-top: 21px; font-style: italic; }

  .contact-list { list-style: none; }
  .contact-item { display: flex; gap: 8px; margin-bottom: 3px; color: var(--text-strong); }
  .contact-item.address { color: var(--text); }
  .contact-icon { flex: 0 0 16px; height: 22px; display: flex; align-items: center; }
  .contact-icon svg { width: 14px; height: 14px; fill: none; stroke: var(--icon); stroke-width: 1.2; }
</style>
</head>
<body>
<footer class="site-footer">
  <section class="footer-col col-about">
    <div class="brand"><span class="brand-mark"></span>Maison Verlaine</div>
    <p class="about-text">Our professional and caring staff is dedicated to working with your family to provide assistance in selecting high quality and affordable funeral services during a time</p>
    <ul class="social-list">
      <li class="social-tile" aria-label="Social link 1"></li>
      <li class="social-tile" aria-label="Social link 2"></li>
      <li class="social-tile" aria-label="Social link 3"></li>
      <li class="social-tile" aria-label="Social link 4"></li>
    </ul>
  </section>

  <section class="footer-col col-testimonials">
    <h2 class="col-heading">Testimonals</h2>
    <blockquote class="testimonial">
      <span class="testimonial-quote-mark">&ldquo;</span>
      <p class="testimonial-body">I wanted to take a moment and thank you again for the very nice service you performed for Ivo's memorial. I had several people come up to me to say "what a wonderful funeral". It was a nice tribute to him."</p>
      <p class="testimonial-author">– Nathan Hollis</p>
    </blockquote>
  </section>

  <section class="footer-col col-contact">
    <h2 class="col-heading">Contact Info</h2>
    <ul class="contact-list">
      <li class="contact-item address">
        <span class="contact-icon"><svg viewBox="0 0 16 16"><path d="M1.5 8 8 2l6.5 6M3.5 6.5V14h3.5v-4h2v4h3.5V6.5"/></svg></span>
        <span>2418 Linden Park Road<br>Fairmont, TX 75012</span>
      </li>
      <li class="contact-item">
        <span class="contact-icon"><svg viewBox="0 0 16 16"><rect x="4.5" y="1.5" width="7" height="13" rx="1"/><path d="M7 12.5h2"/></svg></span>
        <span>(214) 555-0186</span>
      </li>
      <li class="contact-item">
        <span class="contact-icon"><svg viewBox="0 0 16 16"><rect x="1.5" y="3.5" width="13" height="9"/><path d="m1.5 3.5 6.5 5 6.5-5"/></svg></span>
        <span>hello@verlaine-care.com</span>
      </li>
      <li class="contact-item">
        <span class="contact-icon"><svg viewBox="0 0 16 16"><path d="M8 14.5s4.5-4.6 4.5-8a4.5 4.5 0 0 0-9 0c0 3.4 4.5 8 4.5 8z"/><circle cx="8" cy="6.5" r="1.6"/></svg></span>
        <span>Map &amp; Directions</span>
      </li>
    </ul>
  </section>

  <section class="footer-col col-gallery">
    <h2 class="col-heading">Photo Gallery</h2>
  </section>
</footer>
</body>
</html>
```